Broschüren-Design für Unternehmens- und Personalentwicklung
Zielgruppe
Unternehmens- und Personalentwicklung und bieten Seminare, Workshops und Coachings in den Bereichen Führung/Vertrieb und Persönlichkeitsentwicklung an. Wir arbeiten ausschließlich konzeptionell direkt für Unternehmen. Diese kommen aus den unterschiedlichsten Branchen. Übergeordnet sind es alle Branchen mit unserer Zielgruppe Vorstände, Geschäftsführer, Vertriebleiter und Leitung HR bzw. Personalentwicklung.
Aufgabenstellung
Das Design für unsere Broschüre soll im Wiedererkennungswert zu unserem Impulsgeber (Muster anbei) entstehen. Bestandskunden sollen erkennen, dass es was NEUES, doch aber aus unserem Hause ist. Die Herausforderung für das Projekt ist viel mehr, die Umsetzung von vielen Themen in eine leichte, transparente Gestaltung für eine Druckversion. Die Texte werden dazu geliefert. Die Broschüre beginnt klassisch mit einem Deckblatt - auf der Rückseite, also erste Seite innen die Beschreibung, was wir mit dieser erreichen wollen - die zweite Seite innen, wird mit Profilbildern und einem Claim unserer insgesamt 6 Trainer/innen gestaltet werden. Auf der dann folgenden Seite sind unsere drei Rubriken - Vertrieb, Führung und Potentialwachstum kurz beschrieben. In diesem Rubriken gibt es dann zwischen 11 bis 17 Seminarbeschreibungen - vll geriffelt zum raustrennen?! (Muster auch hier anbei) die dargestellt werden. Wichtig ist, dass der Kunde die Option hat, zunächst in seiner von ihm gewünschten Rubrik die einzelnen Seminarbeschreibungen nachlesen zu können. Am Ende der Broschüre sollte eine Call to Action Option sein, wie zum Beispiel eine Postkarte, wo sich der Kunde mehr Informationen oder ein Beratungsgespräch wünscht. Was wir auf keinen Fall wollen, ist ein klassischer Weiterbildungskatalog wie er von Mitbewerben schon seit gefühlten 25 Jahren produziert wird.
Der Auftrag ist hier also auf der einen Seite die pfiffige Gestaltung der Andersartigkeit - und die Kompetenz einer Druckversion zum Auftrag. Womit wir mit den Daten eine Druckerei finden. Zudem muss der Inhalt der Broschüre bzw. die Darstellung der Seminarthemen und Rubriken auf unserer Homepage verwendet werden.
Da wir an ca. 500 Kunden die Broschüre versenden werden, sind ausser den Druckkosten auch die Versandkosten relevant in der Entscheidung. Also Format sehen wir bisher nur die DIN A4 Version .... sind jedoch sehr offen, für alternative Vorschläge zum Format (Bsp. hier auch un..

```html
<!DOCTYPE html>
<html lang="de">
<head>
<meta charset="utf-8">
<title>Broschüre – Deckblatt</title>
<link rel="stylesheet" href="https://fonts.googleapis.com/css2?family=Crimson+Pro:wght@600&family=Open+Sans:wght@300;400&display=swap">
<style>
  :root {
    --backdrop: #272727;
    --paper: #ffffff;
    --brand-blue: #1b80c4;
    --brand-orange: #e9683b;
    --motif-tint: #ececec;
    --text-grey: #5a5a5a;
    --text-light: #808080;
  }
  html, body {
    margin: 0;
    width: 1194px;
    height: 1200px;
    overflow: hidden;
    background: var(--backdrop);
  }
  .cover {
    position: absolute;
    left: 125px;
    top: 117px;
    width: 942px;
    height: 941px;
    background: var(--paper);
    overflow: hidden;
  }
  .ring-motif {
    position: absolute;
    left: -342px;
    top: 52px;
    width: 920px;
    height: 876px;
    border-radius: 50%;
    background: radial-gradient(circle at 50% 50%, var(--motif-tint) 0%, var(--motif-tint) 55%, rgba(236,236,236,0.35) 85%, rgba(236,236,236,0) 100%);
  }
  .accent-disc {
    position: absolute;
    left: -143px;
    top: 342px;
    width: 456px;
    height: 456px;
    border-radius: 50%;
    background: var(--brand-orange);
  }
  .band-graphics {
    position: absolute;
    inset: 0;
  }
  .headline-band {
    position: absolute;
    margin: 0;
    font-family: "Crimson Pro", Georgia, serif;
    font-weight: 600;
    font-size: 48px;
    letter-spacing: 1.5px;
    color: var(--paper);
    line-height: 1;
    display: flex;
    align-items: center;
    justify-content: center;
  }
  .headline-main {
    left: 228px;
    top: 200px;
    width: 651px;
    height: 61px;
  }
  .headline-sub {
    left: 543px;
    top: 289px;
    width: 322px;
    height: 62px;
  }
  .brand {
    position: absolute;
    right: 70px;
    top: 735px;
    text-align: right;
    font-family: "Open Sans", Arial, sans-serif;
  }
  .brand-name {
    margin: 0;
    font-weight: 300;
    font-size: 50px;
    letter-spacing: 0.5px;
    color: var(--text-grey);
    line-height: 1;
  }
  .brand-tagline {
    margin: 16px 14px 0 0;
    text-align: left;
    font-weight: 400;
    font-size: 18px;
    line-height: 1.35;
    color: var(--text-light);
    display: inline-block;
  }
</style>
</head>
<body>
  <main class="cover">
    <div class="ring-motif" role="img" aria-label="Dekoratives Kreislinien-Motiv in hellem Grau"></div>
    <div class="accent-disc" aria-hidden="true"></div>

    <svg class="band-graphics" width="942" height="941" viewBox="0 0 942 941" aria-hidden="true">
      <polygon class="band-blue" points="236,200 879,200 869,261 228,261" fill="var(--brand-blue)"/>
      <polygon class="band-orange" points="551,289 865,289 857,351 543,351" fill="var(--brand-orange)"/>
    </svg>

    <h1 class="headline-band headline-main">PLATZ FÜR EINE HEAD</h1>
    <p class="headline-band headline-sub">HIER IST</p>

    <div class="brand">
      <p class="brand-name">wegbereiter</p>
      <p class="brand-tagline">Unternehmens- und<br>Personalentwicklung</p>
    </div>
  </main>
</body>
</html>
```